Mortgage Broker Site

Need a custom design for a mortgage broker site - please refer to the attached Word .doc that gives more detail.

Number of Pages Required

5+ page

Colors

Designer to choose colors to be used in the design.

```html
<!DOCTYPE html>
<html lang="en">
<head>
<meta charset="utf-8">
<title>Keystead — Mortgage Refinance Loans</title>
<link href="https://fonts.googleapis.com/css2?family=Poppins:wght@400;500;600;700;800&display=swap" rel="stylesheet">
<style>
:root{
  --crimson:#8e0a1e;
  --crimson-deep:#7d0719;
  --slate:#455a76;
  --ink:#111;
  --text:#2a2a2a;
  --hero-bg:#dcdbe9;
  --paper:#f3f3f4;
  --white:#fff;
}
*{box-sizing:border-box;margin:0;padding:0}
html,body{width:1200px;height:2210px;overflow:hidden}
body{position:relative;font-family:"Poppins",sans-serif;color:var(--text);background:var(--white)}
.abs{position:absolute}

/* header */
.brand{left:140px;top:32px;font-size:26px;font-weight:500;color:var(--ink);letter-spacing:-.3px;z-index:3}
.nav{top:44px;font-size:13.5px;font-weight:500;color:var(--ink);z-index:3}
.btn-apply{left:953px;top:40px;width:104px;height:28px;border-radius:14px;background:var(--crimson);color:var(--white);font-size:13px;font-weight:500;display:flex;align-items:center;justify-content:center;z-index:3}

/* hero */
.hero-bg{left:0;top:0;width:1200px;height:580px}
.hero-photo{left:440px;top:0;width:760px;height:570px}
.slider-dot{width:7px;height:7px;border-radius:50%;background:var(--crimson);left:88px}
.slider-dot.active{width:15px;height:15px;left:84px;border:4px solid #b9b8c9}
.hero-title{left:143px;top:152px;font-size:41px;font-weight:800;line-height:56px;color:var(--ink)}
.hero-title .accent{color:var(--crimson)}
.hero-lead{left:144px;top:276px;width:480px;font-size:14.5px;line-height:24px;color:var(--ink)}
.pill{top:354px;height:40px;border-radius:20px;color:var(--white);font-size:12.5px;font-weight:700;display:flex;align-items:center;justify-content:center;letter-spacing:.2px}
.pill.red{left:146px;width:159px;background:var(--crimson)}
.pill.slate{left:325px;width:161px;background:var(--slate)}
.scroll-down{left:607px;top:541px;width:46px;height:46px;border-radius:50%;background:var(--white);box-shadow:0 2px 8px rgba(0,0,0,.15);display:flex;align-items:center;justify-content:center}

/* tools */
.section-title{left:0;width:1200px;text-align:center;font-weight:800;color:var(--ink)}
.section-title .accent{color:var(--crimson)}
.tools-title{top:628px;font-size:29px}
.tools-lead{left:0;top:676px;width:1200px;text-align:center;font-size:13.5px;line-height:24px;color:#333}
.card{overflow:hidden}
.card-left{left:155px;top:795px;width:445px;height:269px;background:linear-gradient(100deg,#e8dedd 0%,#e3d9d7 45%,#d8d6d9 100%)}
.card-right{left:599px;top:755px;width:445px;height:269px;background:linear-gradient(100deg,#e4e7f0 0%,#dde1ea 55%,#cfd3dc 100%)}
.card-icon{position:absolute;width:82px;height:82px;border-radius:8px}
.card h3{position:absolute;font-size:20px;font-weight:800;color:var(--crimson)}
.card p{position:absolute;font-size:13.5px;line-height:24px;color:var(--ink)}
.bracket{border-color:var(--crimson);border-style:solid;width:34px;height:34px}

/* limits */
.limits{left:0;top:1128px;width:1200px;height:412px;background:linear-gradient(110deg,#8c0d22 0%,#a52a41 40%,#9b1b31 70%,#a11f35 100%)}
.limits-sub{top:1196px;left:0;width:1200px;text-align:center;color:var(--white);font-size:16px}
.limits-title{top:1220px;left:0;width:1200px;text-align:center;color:var(--white);font-size:41px;font-weight:800}
.limits-lead{top:1298px;left:340px;width:520px;text-align:center;color:var(--white);font-size:13.5px;line-height:28px}
.search{left:408px;top:1405px;width:385px;height:52px;background:var(--white);border:2px solid #c5566a}
.search span{position:absolute;left:22px;top:14px;font-size:14px;color:#888}
.search .go{left:280px;top:4px;width:100px;height:40px;background:var(--slate);color:var(--white);font-weight:700;font-size:13.5px;display:flex;align-items:center;justify-content:center;position:absolute}

/* connect */
.connect{left:0;top:1540px;width:1200px;height:380px;background:var(--paper)}
.rule-h{height:1px;background:var(--crimson)}
.rule-v{width:1px;background:var(--crimson)}
.connect-sub{left:270px;top:1650px;font-size:20px;color:var(--crimson)}
.connect-title{left:270px;top:1676px;font-size:29px;font-weight:800;color:var(--ink)}
.phone-btn{left:686px;top:1666px;width:261px;height:55px;background:var(--crimson);color:var(--white);font-size:21px;font-weight:700;display:flex;align-items:center;gap:26px;padding-left:22px}
.skyline{left:0;top:1795px;width:1200px;height:125px;background:linear-gradient(180deg,#dfe3ea 0%,#c4cedb 45%,#455a76 75%)}

/* footer */
.footer{left:0;top:1918px;width:1200px;height:292px;background:var(--slate)}
.foot-brand{left:157px;top:1998px;font-size:28px;font-weight:500;color:var(--white)}
.social{top:2069px;width:19px;height:19px}
.copy{left:157px;top:2108px;font-size:10px;line-height:19px;color:#e6e9ef}
.copy b{font-weight:700}
.foot-col{top:2000px;color:var(--white)}
.foot-col h4{font-size:14px;font-weight:700;margin-bottom:10px;letter-spacing:.2px}
.foot-col li{list-style:none;font-size:12px;line-height:24px;color:#eef0f4}
</style>
</head>
<body>

<!-- Hero -->
<svg class="abs hero-bg" width="1200" height="580" viewBox="0 0 1200 580">
  <path d="M0 0H1200V485L630 566L0 485Z" fill="var(--hero-bg)"/>
  <path d="M160 502L630 566L1200 485L1200 490L630 570L160 505Z" fill="var(--slate)"/>
</svg>
<div class="abs hero-photo" role="img" aria-label="Smiling family of three on a sofa, father holding up house keys"
     style="background:linear-gradient(100deg,rgba(220,219,233,0) 0%,#d8d2cd 30%,#c9bfb4 60%,#6f7380 100%);clip-path:polygon(0 0,100% 0,100% 85%,33% 99%,0 94%)"></div>

<div class="abs brand">Keystead</div>
<div class="abs nav" style="left:297px">Rates</div>
<div class="abs nav" style="left:363px">Purchase</div>
<div class="abs nav" style="left:451px">Refinance</div>
<div class="abs nav" style="left:763px">Schedule a Call</div>
<div class="abs nav" style="left:889px">Guide</div>
<div class="abs btn-apply">Apply Now</div>

<span class="abs slider-dot" style="top:213px"></span>
<span class="abs slider-dot active" style="top:240px"></span>
<span class="abs slider-dot" style="top:275px"></span>

<h1 class="abs hero-title"><span class="accent">Mortgage</span><br>Refinance Loans</h1>
<p class="abs hero-lead">Lorem ipsum dolor sit amet, consectetur adipiscing elit, sed do eiusmod tempor incididunt ut labore et dolore</p>
<div class="abs pill red">PURCHASE RATES</div>
<div class="abs pill slate">REFINANCE RATES</div>

<div class="abs scroll-down">
  <svg width="14" height="9" viewBox="0 0 14 9"><path d="M1 1l6 6 6-6" fill="none" stroke="var(--crimson)" stroke-width="2"/></svg>
</div>

<!-- Mortgage tools -->
<h2 class="abs section-title tools-title"><span class="accent">Mortgage</span> Tools</h2>
<p class="abs tools-lead">Lorem ipsum dolor sit amet, consectetur adipiscing elit, sed do eiusmod<br>tempor incididunt ut labore et dolore</p>

<div class="abs bracket" style="left:148px;top:789px;border-width:4px 0 0 4px"></div>
<div class="abs card card-left" role="img" aria-label="Desk with calculator, house model, glasses and loan papers">
  <div class="card-icon" role="img" aria-label="Calculator and money bag icon" style="left:34px;top:32px;background:#b9c8a4"></div>
  <h3 style="left:34px;top:138px">Mortgage Calculator</h3>
  <p style="left:33px;top:176px;width:270px">See how much you can afford by home price, Monthly Payment, or Income</p>
</div>

<div class="abs card card-right" role="img" aria-label="Coins, house model with key and a mortgage application form">
  <div class="card-icon" role="img" aria-label="House with coins and calculator icon" style="left:42px;top:44px;background:#d9a3ad"></div>
  <h3 style="left:44px;top:146px">Home Value Checker</h3>
  <p style="left:43px;top:182px;width:330px">Should you refinance? This calculator breaks down monthly and lifetime cost</p>
</div>
<div class="abs bracket" style="left:1017px;top:995px;border-width:0 4px 4px 0"></div>

<!-- Loan limits -->
<div class="abs limits" role="img" aria-label="Couple signing loan papers beside a small house model, under a red tint"></div>
<p class="abs limits-sub">2019 Mortgage Loan Limits For</p>
<h2 class="abs limits-title">Conventional, FHA, &amp; VA Loans</h2>
<p class="abs limits-lead">Mortgage loan limits for every U.S. county, as published by Federal Home Trust &amp; National Mortgage Board, the Federal Housing Administration (FHA), and the Department of Veterans Affairs (VA)</p>
<div class="abs search"><span>your search...</span><div class="go">SEARCH</div></div>

<!-- Connect -->
<div class="abs connect"></div>
<div class="abs rule-h" style="left:157px;top:1619px;width:486px"></div>
<div class="abs rule-v" style="left:190px;top:1600px;height:123px"></div>
<p class="abs connect-sub">Connect with America’s</p>
<h2 class="abs connect-title">Lending Experts Today!</h2>
<div class="abs phone-btn">
  <svg width="26" height="26" viewBox="0 0 24 24"><path d="M6.6 2.5l3 3.2-1.8 2.6c1 2.3 3.6 4.9 5.9 5.9l2.6-1.8 3.2 3-1.6 3.3C12 18.6 5.4 12 3.3 4.1z" fill="none" stroke="#fff" stroke-width="1.6" stroke-linejoin="round"/></svg>
  <span>(800) 555-0142</span>
</div>
<div class="abs rule-v" style="left:1033px;top:1660px;height:123px"></div>
<div class="abs rule-h" style="left:581px;top:1763px;width:486px"></div>

<div class="abs skyline" role="img" aria-label="Row of suburban houses in front of a pale city skyline"></div>

<!-- Footer -->
<div class="abs footer"></div>
<div class="abs foot-brand">Keystead</div>
<span class="abs social" style="left:157px;background:#3b5ba0"></span>
<span class="abs social" style="left:189px;background:#1da1f2"></span>
<span class="abs social" style="left:221px;background:#d0202c"></span>
<span class="abs social" style="left:253px;background:#f26522"></span>
<p class="abs copy">2009-2019 Copyright <b>Keystead, Inc.</b><br>All rights reserved.</p>

<div class="abs foot-col" style="left:423px">
  <h4>LINKS</h4>
  <ul><li>Get a Mortgage Rate Now</li><li>Loan Types</li><li>Keystead Disclosures</li><li>Conforming, VA &amp; FHA Loan Limits</li></ul>
</div>
<div class="abs foot-col" style="left:683px">
  <h4>COMPANY</h4>
  <ul><li>About Us</li><li>Careers</li><li>Keystead Resources</li><li>Contact</li></ul>
</div>
<div class="abs foot-col" style="left:882px">
  <h4>POLICIES</h4>
  <ul><li>Security Policy</li><li>Privacy Policy</li><li>Terms of Use</li><li>Email Policy</li></ul>
</div>

</body>
</html>
```